TV - business card

Tidewell Vantage is an insurance brokerage firm, inovative, proactive, vigorous, which aims to become the leader of the insurance brokers in Anfrica. We should like to get some designs which should be avoided also in Gray / Metallic for the Administration and Orange / Blue for the Managers (ike in the picture sent). The Blue / Green logo is not the correct one, but the source of the file. Please adjust the color accordingly for the business cards. 1 / Orange / Blue 2 / Gray / Metallic We want something classic but which is transmitted strenght, inovation, modernity and most of all, rapidity. We want something start-up like, very punchy and catching eye remaining profesional at the same time. Name: Delton Ashgrove Function: Managing Director Address: N ° 73/74 Cmt. Bolembe - R / C 2B Esquerda - Bairro Quimbuta - Luanda Tel: (+244) 947 385 619 Email: delton.ashgrove@tidewell-v.com Website: www.tidewell-v. com We want classic in the front and creative, colorfull at the back. The cards will be printed in relief, with very high quality of paper.
Industry/Entity Type
Insurance Broker
Colors
Designer to choose colors to be used in the design.
Look and feel

```html
<!DOCTYPE html>
<html lang="en">
<head>
<meta charset="utf-8">
<title>Tidewell Vantage – Business Card</title>
<link rel="stylesheet" href="https://fonts.googleapis.com/css2?family=Lora:ital,wght@0,400;1,400&family=Montserrat:wght@400;500;700&display=swap">
<style>
  :root {
    --stage: #9c9c9c;
    --stage-light: #c4c4c4;
    --card-dark: #3b3c3e;
    --card-light: #f1f1f1;
    --ink: #1f1f1f;
    --ink-soft: #555555;
    --brand-blue: #3a8ad6;
    --brand-orange: #ec7a34;
    --frame-dark: #2b2b2b;
    --mark-grey: #6b6b6d;
  }
  * { box-sizing: border-box; margin: 0; padding: 0; }
  html, body { width: 1200px; height: 1000px; overflow: hidden; }
  body {
    position: relative;
    background: radial-gradient(ellipse at 50% 40%, var(--stage-light), var(--stage));
    font-family: "Montserrat", Arial, sans-serif;
  }

  /* ---------- Back of card ---------- */
  .card-back {
    position: absolute;
    left: 280px; top: 60px;
    width: 640px; height: 366px;
    background: var(--card-dark);
    box-shadow: 0 8px 22px rgba(0,0,0,.35);
  }
  .card-back__frame-outer {
    position: absolute; inset: 16px 24px;
    border: 2px solid var(--brand-orange);
  }
  .card-back__frame-inner {
    position: absolute; inset: 24px 32px;
    border: 2px solid var(--brand-blue);
  }
  .card-back__mark {
    position: absolute; left: 0; right: 0; top: 50%;
    transform: translateY(-50%);
    display: flex; align-items: center; justify-content: center; gap: 14px;
    color: var(--mark-grey);
    font-weight: 700; font-size: 26px; letter-spacing: 1px; text-transform: uppercase;
  }
  .card-back__mark-dot {
    width: 40px; height: 40px; border-radius: 50%;
    border: 5px solid var(--mark-grey);
  }

  /* ---------- Front of card ---------- */
  .card-front {
    position: absolute;
    left: 210px; top: 470px;
    width: 780px; height: 446px;
    background: var(--card-light);
    box-shadow: 0 10px 26px rgba(0,0,0,.35);
  }
  .card-front__frame-outer {
    position: absolute; inset: 14px 18px;
    border: 2px solid var(--frame-dark);
  }
  .card-front__frame-inner {
    position: absolute; inset: 22px 26px;
    border: 2px solid var(--frame-dark);
  }
  .card-front__watermark {
    position: absolute; left: 110px; top: 88px;
    width: 250px; height: 250px; border-radius: 50%;
    border: 26px solid rgba(0,0,0,.045);
  }
  .holder {
    position: absolute; left: 96px; top: 80px;
  }
  .holder__name {
    font-family: "Lora", Georgia, serif;
    font-style: italic;
    font-size: 38px; color: var(--brand-blue);
  }
  .holder__role {
    font-family: "Lora", Georgia, serif;
    font-style: italic;
    font-size: 16px; color: var(--ink-soft);
    margin-top: 4px; margin-left: 4px;
  }
  .contact-list {
    position: absolute; left: 80px; top: 186px;
    list-style: none;
  }
  .contact-list__item {
    display: flex; align-items: flex-start; gap: 12px;
    font-size: 15px; color: var(--ink); line-height: 1.3;
    margin-bottom: 18px;
  }
  .contact-list__icon { width: 28px; height: 28px; flex: none; }
  .contact-list__text { padding-top: 4px; }
  .divider {
    position: absolute; left: 432px; top: 134px;
    width: 2px; height: 112px; background: var(--ink);
  }
  .brand-mark {
    position: absolute; left: 470px; top: 170px; width: 250px;
    display: flex; flex-direction: column; align-items: center; gap: 12px;
  }
  .brand-mark__dot {
    width: 52px; height: 52px; border-radius: 50%;
    border: 5px solid var(--brand-orange);
  }
  .brand-mark__name {
    font-weight: 700; font-size: 20px; color: var(--brand-orange);
    text-transform: uppercase; white-space: nowrap;
  }
  .website {
    position: absolute; left: 0; right: 0; bottom: 50px;
    text-align: center;
    font-family: "Lora", Georgia, serif; font-size: 18px; color: var(--ink);
  }
  .website__domain { color: var(--brand-blue); }
</style>
</head>
<body>

  <section class="card-back" aria-label="Business card, back">
    <div class="card-back__frame-outer"></div>
    <div class="card-back__frame-inner"></div>
    <div class="card-back__mark">
      <span class="card-back__mark-dot"></span>
      <span>Tidewell Vantage</span>
    </div>
  </section>

  <section class="card-front" aria-label="Business card, front">
    <div class="card-front__frame-outer"></div>
    <div class="card-front__frame-inner"></div>
    <div class="card-front__watermark"></div>

    <div class="holder">
      <h1 class="holder__name">Delton Ashgrove</h1>
      <p class="holder__role">Managing Director</p>
    </div>

    <ul class="contact-list">
      <li class="contact-list__item">
        <svg class="contact-list__icon" viewBox="0 0 28 28" aria-hidden="true">
          <circle cx="14" cy="14" r="11" fill="none" stroke="var(--brand-blue)" stroke-width="2"/>
          <path d="M9.5 8.5l2.5-.5 1.3 3-1.5 1.2a8 8 0 0 0 3.7 3.7l1.2-1.5 3 1.3-.5 2.5c-5.5.3-10-4.2-9.7-9.7z" fill="var(--brand-blue)"/>
        </svg>
        <span class="contact-list__text">(+244) 947 385 619</span>
      </li>
      <li class="contact-list__item">
        <svg class="contact-list__icon" viewBox="0 0 28 28" aria-hidden="true">
          <circle cx="14" cy="14" r="11" fill="none" stroke="var(--brand-blue)" stroke-width="2"/>
          <rect x="8.5" y="10" width="11" height="8" rx="1" fill="var(--brand-blue)"/>
          <path d="M8.8 10.5l5.2 4 5.2-4" fill="none" stroke="#fff" stroke-width="1.2"/>
        </svg>
        <span class="contact-list__text">delton.ashgrove@tidewell-v.com</span>
      </li>
      <li class="contact-list__item">
        <svg class="contact-list__icon" viewBox="0 0 28 28" aria-hidden="true">
          <circle cx="14" cy="14" r="11" fill="none" stroke="var(--brand-blue)" stroke-width="2"/>
          <path d="M14 7.5a4.5 4.5 0 0 0-4.5 4.5c0 3.4 4.5 8.5 4.5 8.5s4.5-5.1 4.5-8.5A4.5 4.5 0 0 0 14 7.5z" fill="var(--brand-blue)"/>
          <circle cx="14" cy="12" r="1.7" fill="#fff"/>
        </svg>
        <span class="contact-list__text">N° 73/74 Cmt. Bolembe - R / C 2B<br>Esquerda - Bairro Quimbuta - Luanda</span>
      </li>
    </ul>

    <div class="divider"></div>

    <div class="brand-mark">
      <span class="brand-mark__dot"></span>
      <span class="brand-mark__name">Tidewell Vantage</span>
    </div>

    <p class="website">www.<span class="website__domain">tidewell-v</span>.com</p>
  </section>

</body>
</html>
```